Business Card Design Project

Name: Kunle O. Edet
Designation: Partner
Address: QRM Building, 14 Harmony Close, P.O. Box 58314, Victoria Island Lagos, Nigeria
Tel: +234 1 7395162
mobile: +234 1 7061527394
Email: koedet@larkmoorassociates.com
website www.larkmoorassociates.com

```html
<!DOCTYPE html>
<html lang="en">
<head>
<meta charset="utf-8">
<title>Larkmoor Associates – Business Card</title>
<link rel="stylesheet" href="https://fonts.googleapis.com/css2?family=Open+Sans:wght@400;600;700&display=swap">
<style>
  :root {
    --page-bg: #8f8f8f;
    --card-light: #ffffff;
    --card-shade: #e4e4e4;
    --band-dark: #000000;
    --band-mid: #2a2a2a;
    --ink: #1e1e1e;
    --ink-soft: #444444;
    --band-text: #ffffff;
    --band-text-soft: #d6d6d6;
    --divider: #c9c9c9;
  }
  * { box-sizing: border-box; margin: 0; padding: 0; }
  html, body {
    width: 1200px; height: 1200px; overflow: hidden;
    background: var(--page-bg);
    font-family: "Open Sans", sans-serif;
  }
  .sheet {
    width: 1200px; height: 1200px;
    display: flex; flex-direction: column; align-items: center; justify-content: center;
    gap: 60px;
  }
  .card {
    position: relative;
    width: 700px; height: 400px;
    background: linear-gradient(135deg, var(--card-light) 0%, #f4f4f4 45%, var(--card-shade) 100%);
    box-shadow: 0 10px 24px rgba(0,0,0,0.28);
    overflow: hidden;
  }
  /* Front */
  .card-front .brand {
    position: absolute; left: 0; right: 0; top: 0; bottom: 0;
    display: flex; align-items: center; justify-content: center; gap: 18px;
  }
  .brand-dot {
    width: 54px; height: 54px; border-radius: 50%;
    background: linear-gradient(180deg, #9a9a9a, #3a3a3a);
  }
  .brand-name {
    font-weight: 600; font-size: 44px; color: var(--ink); letter-spacing: 0.5px;
  }
  /* Back */
  .band {
    position: absolute; left: 0; top: 0; width: 100%; height: 150px;
    background: linear-gradient(180deg, var(--band-mid) 0%, var(--band-dark) 40%);
  }
  .band .brand {
    position: absolute; left: 34px; top: 30px;
    display: flex; align-items: center; gap: 12px;
  }
  .band .brand-dot { width: 34px; height: 34px; background: linear-gradient(180deg, #f0f0f0, #8a8a8a); }
  .band .brand-name { font-size: 26px; color: var(--band-text-soft); }
  .holder {
    position: absolute; right: 36px; top: 78px; text-align: right; color: var(--band-text);
  }
  .holder-name { font-size: 28px; font-weight: 400; letter-spacing: 1px; line-height: 1.1; }
  .holder-name strong { font-weight: 700; }
  .holder-role { font-size: 24px; letter-spacing: 1px; line-height: 1.2; color: var(--band-text-soft); }
  .details {
    position: absolute; top: 175px; left: 0; width: 100%; bottom: 0;
    display: flex;
  }
  .col { padding: 0 30px; font-size: 16px; color: var(--ink); line-height: 1.35; }
  .col-left { width: 52%; padding-left: 60px; }
  .col-right { width: 48%; border-left: 1px solid var(--divider); padding-top: 88px; }
  .line { display: flex; align-items: flex-start; gap: 8px; }
  .line + .line { margin-top: 2px; }
  .gap { margin-top: 12px; }
  .icon { width: 14px; height: 14px; flex: none; margin-top: 3px; }
</style>
</head>
<body>
<main class="sheet">

  <section class="card card-front" aria-label="Card front">
    <div class="brand">
      <span class="brand-dot"></span>
      <span class="brand-name">Larkmoor Associates</span>
    </div>
  </section>

  <section class="card card-back" aria-label="Card back">
    <header class="band">
      <div class="brand">
        <span class="brand-dot"></span>
        <span class="brand-name">Larkmoor Associates</span>
      </div>
      <div class="holder">
        <p class="holder-name">Kunle O. <strong>Edet</strong></p>
        <p class="holder-role">Partner</p>
      </div>
    </header>

    <div class="details">
      <div class="col col-left">
        <div class="line">
          <svg class="icon" viewBox="0 0 14 14"><ellipse cx="7" cy="3" rx="6" ry="2" fill="#333"/><ellipse cx="7" cy="7" rx="6" ry="2" fill="#555"/><ellipse cx="7" cy="11" rx="6" ry="2" fill="#333"/></svg>
          <span>QRM Building, 14 Harmony Close,<br>P.O. Box 58314,<br>Victoria Island Lagos, Nigeria</span>
        </div>
        <div class="line gap">
          <svg class="icon" viewBox="0 0 14 14"><path d="M3 1 L5 4 L4 6 Q6 9 8 10 L10 9 L13 11 L11 13 Q5 12 1 3 Z" fill="#333"/></svg>
          <span>Tel: +234 1 7395162</span>
        </div>
        <div class="line">
          <svg class="icon" viewBox="0 0 14 14"><rect x="3" y="1" width="8" height="12" rx="1.5" fill="#333"/><rect x="4.5" y="3" width="5" height="5" fill="#ddd"/></svg>
          <span>Mobile: +234 1 7061527394</span>
        </div>
      </div>
      <div class="col col-right">
        <div class="line">
          <svg class="icon" viewBox="0 0 14 14"><rect x="1" y="3" width="12" height="8" fill="#333"/><path d="M1 3 L7 8 L13 3" stroke="#ddd" stroke-width="1" fill="none"/></svg>
          <span>koedet@larkmoorassociates.com</span>
        </div>
        <div class="line">
          <svg class="icon" viewBox="0 0 14 14"><circle cx="7" cy="7" r="6" fill="none" stroke="#333" stroke-width="1.3"/><ellipse cx="7" cy="7" rx="2.5" ry="6" fill="none" stroke="#333"/><line x1="1" y1="7" x2="13" y2="7" stroke="#333"/></svg>
          <span>www.larkmoorassociates.com</span>
        </div>
      </div>
    </div>
  </section>

</main>
</body>
</html>
```